Life Changing Hypnosis Practitioner Business card

I have launched a logo project at the same time as this project.
1- AWAKEN is the main word
2- Inner Tide in smaller letters
3- Hypnosis bold or same as Awaken.
eye catching and bold in design

Target Market(s)

Everyone

Font styles to use
Sans Serif

Colors
add136
0255a3
ec2027

Requirements
Must have
• Blue and green and maybe black in colour must be eye catching and bold.
Nice to have
• interesting in its look
Should not have
• Plain and boring

```html
<!DOCTYPE html>
<html lang="en">
<head>
<meta charset="utf-8">
<title>Awaken – Inner Tide Hypnosis Business Card</title>
<link rel="stylesheet" href="https://fonts.googleapis.com/css2?family=Montserrat:wght@400;600;700&display=swap">
<style>
  :root {
    --stage: #3a3a3a;
    --card: #272324;
    --band: #312d2e;
    --accent-red: #ec2027;
    --accent-blue: #0255a3;
    --accent-green: #add136;
    --ink: #ffffff;
  }
  * { box-sizing: border-box; margin: 0; padding: 0; }
  html, body {
    width: 1200px; height: 799px; overflow: hidden;
    background: var(--stage);
    font-family: "Montserrat", sans-serif;
  }
  .stage { position: relative; width: 1200px; height: 799px; }
  .card {
    position: absolute; top: 257px;
    width: 500px; height: 285px;
    background: var(--card);
    overflow: hidden;
    box-shadow: 0 14px 30px rgba(0,0,0,.45);
  }
  .card--front { left: 80px; }
  .card--back { left: 620px; }
  .band { position: absolute; left: 0; right: 0; background: var(--band); }
  .card--front .band--top { top: 0; height: 50px; }
  .card--front .band--lower { top: 190px; height: 65px; }
  .card--back .band--info { top: 118px; height: 100px; }
  .bar { position: absolute; height: 9px; background: var(--accent-blue); }
  .bar--top { top: 0; left: 150px; width: 215px; }
  .bar--bottom { bottom: 0; left: 50px; width: 225px; }

  .brand {
    position: absolute; display: flex; align-items: center;
    color: var(--accent-red);
  }
  .brand__mark { flex: none; background: var(--accent-green); }
  .brand__text { display: flex; flex-direction: column; align-items: center; line-height: 1; }
  .brand__name { font-weight: 600; letter-spacing: 3px; }
  .brand__tag { font-weight: 600; letter-spacing: 2px; margin-top: 6px; }

  .card--front .brand { top: 95px; left: 0; right: 0; justify-content: center; gap: 14px; }
  .card--front .brand__mark { width: 14px; height: 14px; }
  .card--front .brand__name { font-size: 38px; }
  .card--front .brand__tag { font-size: 13px; }

  .card--back .brand { top: 48px; left: 260px; transform: translateX(-50%); gap: 10px; }
  .card--back .brand__mark { width: 10px; height: 10px; }
  .card--back .brand__name { font-size: 25px; }
  .card--back .brand__tag { font-size: 9px; margin-top: 5px; }

  .holder {
    position: absolute; top: 154px; left: 40px; width: 190px;
    text-align: right; color: var(--ink); font-weight: 700; font-size: 20px;
  }
  .divider {
    position: absolute; top: 138px; left: 245px; width: 2px; height: 56px;
    background: var(--ink);
  }
  .contacts {
    position: absolute; top: 134px; left: 258px; list-style: none;
    color: var(--ink); font-size: 13px; line-height: 17px;
  }
  .contacts li { display: flex; align-items: center; gap: 5px; white-space: nowrap; }
  .contacts svg { width: 9px; height: 9px; flex: none; }
</style>
</head>
<body>
<main class="stage">
  <section class="card card--front" aria-label="Card front">
    <div class="band band--top"></div>
    <div class="band band--lower"></div>
    <div class="brand">
      <span class="brand__mark"></span>
      <div class="brand__text">
        <span class="brand__name">AWAKEN</span>
        <span class="brand__tag">Inner Tide Hypnosis</span>
      </div>
    </div>
  </section>

  <section class="card card--back" aria-label="Card back">
    <div class="bar bar--top"></div>
    <div class="band band--info"></div>
    <div class="brand">
      <span class="brand__mark"></span>
      <div class="brand__text">
        <span class="brand__name">AWAKEN</span>
        <span class="brand__tag">Inner Tide Hypnosis</span>
      </div>
    </div>
    <p class="holder">Your Name</p>
    <div class="divider"></div>
    <ul class="contacts">
      <li><svg viewBox="0 0 10 10"><circle cx="5" cy="5" r="4.2" fill="none" stroke="#fff" stroke-width="1"/></svg>+1 (555) 014 2270</li>
      <li><svg viewBox="0 0 10 10"><circle cx="5" cy="5" r="4.2" fill="none" stroke="#fff" stroke-width="1"/></svg>hello@innertide.com</li>
      <li><svg viewBox="0 0 10 10"><circle cx="5" cy="5" r="4.2" fill="none" stroke="#fff" stroke-width="1"/></svg>www.innertide.com</li>
      <li><svg viewBox="0 0 10 10"><circle cx="5" cy="5" r="4.2" fill="none" stroke="#fff" stroke-width="1"/></svg>www.innertidehypnosis.com</li>
    </ul>
    <div class="bar bar--bottom"></div>
  </section>
</main>
</body>
</html>
```